Delcourt Realty Business Cards

Design business card

Target Market(s)

High-End Buyer of Real Estate over $1 million dollars

Industry/Entity Type

Realtor

Contact Information for Business Card

Lena Delcourt R(S) LIC.# 41972
Cell 555 246-1938
Email Lena@Delcourt.example
Website IsleFreshHomes.example

Also Need Cards for:

Hank Delcourt R(B) LIC# 69418
C 555 613-7052
E Hank@Delcourt.example
W IsleFreshHomes.example

Colors

Designer to choose colors to be used in the design.

Requirements
Must have
• Address on back:
• 287 Pohaku Cir. , Lanakila Bay HI 96700
• Logo on back
Nice to have
• I would like the phone numbers and email address to be big so people can read it easily
Should not have
• Very small print Except For: address (287 Pohaku Cir. Wailea HI 96753)

```html
<!DOCTYPE html>
<html lang="en">
<head>
<meta charset="utf-8">
<title>Delcourt Realty Business Cards</title>
<link href="https://fonts.googleapis.com/css2?family=Open+Sans:wght@400;600;700&display=swap" rel="stylesheet">
<style>
  :root {
    --backdrop: #2b2d31;
    --card-white: #ffffff;
    --card-grey: #dcdcdc;
    --band-grey: #8c8c8c;
    --ink-grey: #7a7a7a;
    --ink-dark: #111111;
    --photo-pink: #d81b72;
    --photo-dark: #161616;
    --photo-skin: #c9a58a;
  }
  * { box-sizing: border-box; margin: 0; padding: 0; }
  html, body { width: 1200px; height: 900px; overflow: hidden; }
  body {
    background: var(--backdrop);
    font-family: "Open Sans", sans-serif;
    position: relative;
  }
  .card {
    position: absolute;
    top: 150px;
    width: 343px;
    height: 600px;
    border-radius: 26px;
    overflow: hidden;
  }
  /* Contact side */
  .card-contact { left: 220px; background: var(--card-white); }
  .brand-mark {
    position: absolute;
    top: 78px; left: 0; right: 0;
    display: flex; align-items: center; justify-content: center; gap: 10px;
    color: var(--ink-grey);
    font-weight: 600;
    font-size: 17px;
    letter-spacing: 1.5px;
    text-transform: uppercase;
  }
  .brand-square { width: 26px; height: 26px; background: var(--ink-grey); border-radius: 3px; }
  .name-band {
    position: absolute;
    top: 160px; left: 0; right: 0;
    height: 88px;
    background: var(--band-grey);
    color: var(--card-white);
    text-align: center;
    padding-top: 16px;
  }
  .agent-name { font-size: 27px; font-weight: 700; line-height: 1.15; }
  .agent-license { font-size: 18px; font-weight: 400; }
  .contact-list {
    position: absolute;
    top: 282px; left: 0; right: 0;
    display: flex; flex-direction: column; align-items: center;
    color: var(--ink-grey);
    text-align: center;
  }
  .contact-icon { width: 46px; height: 46px; display: block; }
  .contact-line { font-size: 24px; margin: 4px 0 14px; }
  .contact-line.email { font-size: 20px; }
  .contact-address { font-size: 15px; margin-top: 26px; }

  /* Photo side */
  .card-photo { left: 640px; background: var(--card-grey); }
  .brand-block {
    position: absolute;
    top: 80px; left: 0; right: 0;
    display: flex; align-items: center; justify-content: center; gap: 12px;
    color: var(--ink-dark);
    font-weight: 700;
    font-size: 22px;
    letter-spacing: 2px;
    text-transform: uppercase;
  }
  .brand-block .brand-square { width: 34px; height: 34px; background: var(--ink-dark); }
  .team-photo {
    position: absolute;
    right: 0; bottom: 0;
    width: 250px; height: 350px;
    background:
      linear-gradient(200deg, var(--photo-dark) 0%, var(--photo-dark) 30%, rgba(22,22,22,0) 55%),
      linear-gradient(180deg, var(--card-grey) 0%, var(--photo-skin) 45%, var(--photo-pink) 80%, var(--photo-pink) 100%);
  }
</style>
</head>
<body>
  <section class="card card-contact">
    <div class="brand-mark"><span class="brand-square"></span>Delcourt Realty</div>
    <div class="name-band">
      <p class="agent-name">Lena Delcourt</p>
      <p class="agent-license">R(S) LIC.# 41972</p>
    </div>
    <div class="contact-list">
      <svg class="contact-icon" viewBox="0 0 46 46" aria-hidden="true">
        <circle cx="23" cy="23" r="21" fill="none" stroke="#7a7a7a" stroke-width="2"/>
        <path d="M16 15c1-1 3-1 4 0l2 3c1 1 0 2-1 3 1 2 3 4 5 5 1-1 2-2 3-1l3 2c1 1 1 3 0 4-2 2-5 2-8 0-4-2-7-5-9-9-1-3-1-5 1-7z" fill="#7a7a7a"/>
      </svg>
      <p class="contact-line">555 246-1938</p>
      <svg class="contact-icon" viewBox="0 0 46 46" aria-hidden="true">
        <circle cx="23" cy="23" r="21" fill="none" stroke="#7a7a7a" stroke-width="2"/>
        <rect x="13" y="16" width="20" height="14" fill="none" stroke="#7a7a7a" stroke-width="2"/>
        <path d="M13 16l10 8 10-8" fill="none" stroke="#7a7a7a" stroke-width="2"/>
      </svg>
      <p class="contact-line email">Lena@Delcourt.example</p>
      <svg class="contact-icon" viewBox="0 0 46 46" aria-hidden="true">
        <circle cx="23" cy="23" r="21" fill="none" stroke="#7a7a7a" stroke-width="2"/>
        <path d="M23 35c-5-6-8-10-8-14a8 8 0 0 1 16 0c0 4-3 8-8 14z" fill="none" stroke="#7a7a7a" stroke-width="2"/>
        <circle cx="23" cy="21" r="3" fill="#7a7a7a"/>
      </svg>
      <p class="contact-address">287 Pohaku Cir. , Lanakila Bay HI 96700</p>
    </div>
  </section>

  <section class="card card-photo">
    <div class="brand-block"><span class="brand-square"></span>Delcourt Realty</div>
    <div class="team-photo" role="img" aria-label="Portrait photo of the two Delcourt agents, a woman in pink and a man in a dark jacket"></div>
  </section>
</body>
</html>
```